Vira Nostalma is a dietary supplement company and in need of label design for 4 products

label for 4 dietary supplement products :1- Biotin. Red bottle ( please see the picture attached, not the whole bottle is colored but rather its a white bottle with the upper part and lower part of the bottle colored)2- COQ10. Orange Bottle 3- Hair Skin Nail. Pink bottle 4- Probiotics. Green Bottle we like the label to:1- have a modern and sleek appearance with very limited graphics.2- have a transparent background( as the bottle is white )3- have the box with the supplement and ingredient to appear sideways( horizontal )4- to have a color matching the bottle color.attached you will find :1- the dimension of the bottle.2- four different labels for each of the products.3- two pictures of the bottles 4- picture of the caps5- Logo
Industry/Entity Type
Health And Wellness
Colors
Designer to choose colors to be used in the design.
Look and feel
Each slider illustrates characteristics of the customer's brand and the style your logo design should communicate.

```html
<!DOCTYPE html>
<html lang="en">
<head>
<meta charset="utf-8">
<title>Vira Nostalma — Supplement Labels</title>
<link href="https://fonts.googleapis.com/css2?family=Roboto:wght@300;400;500&family=Nunito:wght@600;700&display=swap" rel="stylesheet">
<style>
  :root {
    --bg-top: #e6e6e6;
    --bg-mid: #ffffff;
    --label: #f7f5f6;
    --ink: #2a2a2a;
    --muted: #555555;
    --brand: #2b3a2f;
    --biotin: #e31e24;
    --coq10: #f07c1e;
    --probiotic: #1f9a45;
    --probiotic-band: #2d5a2e;
    --hsn: #e0168f;
    --hsn-title: #c43a9e;
  }
  * { box-sizing: border-box; margin: 0; padding: 0; }
  html, body { width: 1200px; height: 1008px; overflow: hidden; }
  body {
    background: linear-gradient(to bottom, var(--bg-top) 0%, var(--bg-mid) 25%, var(--bg-mid) 82%, #d9d9d9 100%);
    font-family: "Roboto", sans-serif;
    position: relative;
  }
  .label-row {
    position: absolute;
    left: 146px;
    top: 300px;
    display: flex;
    gap: 35px;
  }
  .label {
    width: 202px;
    height: 430px;
    background: var(--label);
    border-radius: 6px;
    box-shadow: 0 10px 24px rgba(0,0,0,0.12);
    position: relative;
    overflow: hidden;
  }
  .label__band {
    height: 44px;
    background: var(--accent-band, var(--accent));
  }
  .brand {
    margin: 80px auto 0;
    text-align: center;
    font-family: "Nunito", sans-serif;
    font-weight: 700;
    font-size: 21px;
    color: var(--brand);
    letter-spacing: 0.5px;
    display: flex;
    align-items: center;
    justify-content: center;
    gap: 7px;
  }
  .brand__dot {
    width: 9px; height: 9px;
    background: var(--brand);
  }
  .panel {
    position: absolute;
    left: 30px;
    right: 30px;
    top: 225px;
    height: 122px;
    border: 1.2px solid var(--accent);
    text-align: center;
  }
  .panel__title {
    position: absolute;
    left: 50%;
    top: -16px;
    transform: translateX(-50%);
    background: var(--label);
    padding: 0 6px;
    font-family: "Nunito", sans-serif;
    font-weight: 700;
    font-size: 28px;
    line-height: 30px;
    color: var(--title, var(--accent));
    white-space: nowrap;
  }
  .panel__title--small { font-size: 20px; top: -12px; line-height: 22px; }
  .panel__title--stack { font-size: 19px; line-height: 21px; top: -11px; }
  .panel__sub {
    margin-top: 20px;
    font-size: 11.5px;
    font-weight: 400;
    color: var(--ink);
  }
  .panel--stack .panel__sub { margin-top: 36px; font-size: 9px; color: var(--muted); }
  .panel__kind {
    margin-top: 24px;
    font-size: 12px;
    font-weight: 300;
    color: var(--ink);
  }
  .panel--stack .panel__kind { margin-top: 14px; }
  .panel__count {
    position: absolute;
    left: 50%;
    bottom: -10px;
    transform: translateX(-50%);
    background: var(--label);
    padding: 0 5px;
    display: flex;
    align-items: baseline;
    gap: 3px;
    white-space: nowrap;
    font-size: 12px;
    color: var(--ink);
  }
  .panel__count b { font-size: 17px; font-weight: 500; }
  .capsule-icon { width: 13px; height: 12px; align-self: center; }
  .label--biotin { --accent: var(--biotin); }
  .label--coq10 { --accent: var(--coq10); }
  .label--probiotic { --accent: var(--probiotic); --accent-band: var(--probiotic-band); }
  .label--hsn { --accent: var(--hsn); --title: var(--hsn-title); }
</style>
</head>
<body>
  <main class="label-row">
    <section class="label label--biotin">
      <div class="label__band"></div>
      <div class="brand"><span class="brand__dot"></span>Vira Nostalma</div>
      <div class="panel">
        <h2 class="panel__title">Biotin</h2>
        <p class="panel__sub">100% Pure</p>
        <p class="panel__kind">Dietary Supplement</p>
        <p class="panel__count">
          <svg class="capsule-icon" viewBox="0 0 13 12"><rect x="0.5" y="0.5" width="5" height="11" rx="2.5" fill="none" stroke="#444"/><rect x="0.5" y="0.5" width="5" height="5.5" rx="2.5" fill="#444"/><rect x="7.5" y="0.5" width="5" height="11" rx="2.5" fill="none" stroke="#444"/><rect x="7.5" y="0.5" width="5" height="5.5" rx="2.5" fill="#444"/></svg>
          <b>60</b>Capsules
        </p>
      </div>
    </section>

    <section class="label label--coq10">
      <div class="label__band"></div>
      <div class="brand"><span class="brand__dot"></span>Vira Nostalma</div>
      <div class="panel">
        <h2 class="panel__title">COQ10</h2>
        <p class="panel__sub">(UBIQUINONE)</p>
        <p class="panel__kind">Dietary Supplement</p>
        <p class="panel__count">
          <svg class="capsule-icon" viewBox="0 0 13 12"><rect x="0.5" y="0.5" width="5" height="11" rx="2.5" fill="none" stroke="#444"/><rect x="0.5" y="0.5" width="5" height="5.5" rx="2.5" fill="#444"/><rect x="7.5" y="0.5" width="5" height="11" rx="2.5" fill="none" stroke="#444"/><rect x="7.5" y="0.5" width="5" height="5.5" rx="2.5" fill="#444"/></svg>
          Any Count
        </p>
      </div>
    </section>

    <section class="label label--probiotic">
      <div class="label__band"></div>
      <div class="brand"><span class="brand__dot"></span>Vira Nostalma</div>
      <div class="panel">
        <h2 class="panel__title panel__title--small">Probiotic 40</h2>
        <p class="panel__sub">40 BILLION</p>
        <p class="panel__kind">Dietary Supplement</p>
        <p class="panel__count">
          <svg class="capsule-icon" viewBox="0 0 13 12"><rect x="0.5" y="0.5" width="5" height="11" rx="2.5" fill="none" stroke="#444"/><rect x="0.5" y="0.5" width="5" height="5.5" rx="2.5" fill="#444"/><rect x="7.5" y="0.5" width="5" height="11" rx="2.5" fill="none" stroke="#444"/><rect x="7.5" y="0.5" width="5" height="5.5" rx="2.5" fill="#444"/></svg>
          <b>30</b>Capsules
        </p>
      </div>
    </section>

    <section class="label label--hsn">
      <div class="label__band"></div>
      <div class="brand"><span class="brand__dot"></span>Vira Nostalma</div>
      <div class="panel panel--stack">
        <h2 class="panel__title panel__title--stack">Hair, Skin<br>&amp; Nails</h2>
        <p class="panel__sub">ESSENTIALS</p>
        <p class="panel__kind">Dietary Supplement</p>
        <p class="panel__count">
          <svg class="capsule-icon" viewBox="0 0 13 12"><rect x="0.5" y="0.5" width="5" height="11" rx="2.5" fill="none" stroke="#444"/><rect x="0.5" y="0.5" width="5" height="5.5" rx="2.5" fill="#444"/><rect x="7.5" y="0.5" width="5" height="11" rx="2.5" fill="none" stroke="#444"/><rect x="7.5" y="0.5" width="5" height="5.5" rx="2.5" fill="#444"/></svg>
          Any Count
        </p>
      </div>
    </section>
  </main>
</body>
</html>
```